Soy Candle Business needs a label design

We need a label design for a new company selling soy candles - Velvet Hearth Co.

We are using apothecary jars in 3 sizes.
As per attached candles will be dressed with a beautiful black bow and all finished with a diamante in centre of bow.

We would like label done on lid of candle jars - 5cm circle (5cm from one side to the other), this way one label will fit each product size. Label will be done as a sticker.

We are thinking of the background colour to be black, however are open to recommendations. We want label to be classy, elegant and simple.

Inspiration for candle design came from attached invitation that features the bow, and beautiful vintage paper on top area.

Label should include the following 3 pieces of information:
Velvet Hearth Co (company name)
Coconut Lime (this will change depending on fragrance)
Soy Candle

Velvet Hearth Co does not have a company logo... what is done for the label will set tone for what is done across other elements of business moving forward.

Industry/Entity Type

Business

Requirements
Must have
• Velvet Hearth Co
Fragrance Flavour
Soy Candle

```html
<!DOCTYPE html>
<html lang="en">
<head>
<meta charset="utf-8">
<title>Velvet Hearth Co – Soy Candle Lid Labels</title>
<link href="https://fonts.googleapis.com/css2?family=Yellowtail&family=Signika:wght@500&display=block" rel="stylesheet">
<style>
  :root {
    --page: #ffffff;
    --ink: #000000;
    --cream: #fdfbe6;
    --title: #ffffff;
    --fragrance: #b8966a;
    --product: #f2a935;
  }
  html, body {
    margin: 0;
    padding: 0;
    overflow: hidden;
    background: var(--page);
  }
  .canvas {
    width: 1200px;
    height: 579px;
    position: relative;
    overflow: hidden;
    background: var(--page);
  }
  .labels { display: block; }
  .brand-name {
    font-family: "Yellowtail", "Dancing Script", "Brush Script MT", cursive;
    font-size: 44px;
    fill: var(--title);
  }
  .fragrance,
  .product {
    font-family: "Signika", "Trebuchet MS", sans-serif;
    font-weight: 500;
    font-size: 31px;
  }
  .fragrance { fill: var(--fragrance); }
  .product { fill: var(--product); }
  .label-edge { fill: none; stroke: var(--ink); stroke-width: 1.5; }
  .name-plate { fill: var(--ink); }
</style>
</head>
<body>
<div class="canvas">
  <svg class="labels" width="1200" height="579" viewBox="0 0 1200 579" xmlns="http://www.w3.org/2000/svg">
    <defs>
      <radialGradient id="damask-on-black" cx="50%" cy="50%" r="50%">
        <stop offset="0%" stop-color="#6b695c"/>
        <stop offset="60%" stop-color="#4a483f"/>
        <stop offset="100%" stop-color="#2b2a25"/>
      </radialGradient>
      <radialGradient id="damask-on-cream" cx="50%" cy="50%" r="50%">
        <stop offset="0%" stop-color="#b9b7a3"/>
        <stop offset="70%" stop-color="#c9c6b0"/>
        <stop offset="100%" stop-color="#e4e1ca"/>
      </radialGradient>
    </defs>

    <g class="label label--dark">
      <circle class="damask-field" cx="300" cy="291" r="264" fill="url(#damask-on-black)"
              role="img" aria-label="Cream damask pattern on black background"/>
      <circle class="label-edge" cx="300" cy="291" r="264"/>
      <ellipse class="name-plate" cx="300" cy="290" rx="188" ry="104"/>
      <text class="brand-name" x="303" y="269" text-anchor="middle">Velvet Hearth Co</text>
      <text class="fragrance" x="300" y="323" text-anchor="middle">Coconut Lime</text>
      <text class="product" x="300" y="359" text-anchor="middle">Soy Candle</text>
    </g>

    <g class="label label--cream">
      <circle class="damask-field" cx="906" cy="282" r="263" fill="url(#damask-on-cream)"
              role="img" aria-label="Black damask pattern on cream background"/>
      <ellipse class="name-plate" cx="906" cy="280" rx="186" ry="105"/>
      <text class="brand-name" x="909" y="260" text-anchor="middle">Velvet Hearth Co</text>
      <text class="fragrance" x="906" y="311" text-anchor="middle">Coconut Lime</text>
      <text class="product" x="906" y="348" text-anchor="middle">Soy Candle</text>
    </g>
  </svg>
</div>
</body>
</html>
```